Flyer-Design für Autolackiererei
Hallo es muss nur noch die Richtige Telefonnumer rein , die bekomm ich esrt von Fernolux zu geschickt
Zielgruppe
Karosserie & Autolackiererei
Autohäuser , Privatkunden , Bussunterhemen , LKW Unterhemen , Versicherungen
Aufgabenstellung
Neueröffung Von Autolackiererei ab 01.03.2019 bitte ganz wichtig muss auf flayer drauf.
Unfallinstansetztung , Fahrzeuglackierung Jeglicher Art , Oldtimer Restauration , Fahrzeugaufbereitung , Achsvermessung ,Felgen Lackieren ,Hagelschaden ,
inspektionen alle Fahrzeug Fabrikaten, Vexa, Reifenservice
Hol und Bring service ,scheibenaustausch abwicklung mit versicherung ,
Smart Repair

```html
<!DOCTYPE html>
<html lang="de">
<head>
<meta charset="utf-8">
<title>Flyer Autolackiererei Brenner – Neueröffnung</title>
<link rel="stylesheet" href="https://fonts.googleapis.com/css2?family=Bebas+Neue&family=Oswald:wght@300;400&display=swap">
<style>
  :root {
    --blue: #1f95d6;
    --grey: #6f6e6e;
    --grey-text: #5f5e5e;
    --white: #ffffff;
    --page: #ffffff;
    --label: #555555;
  }
  * { box-sizing: border-box; margin: 0; padding: 0; }
  html, body {
    width: 1200px; height: 848px; overflow: hidden;
    background: var(--page);
    font-family: "Oswald", "Arial Narrow", sans-serif;
  }
  .canvas { position: relative; width: 1200px; height: 848px; }

  .side-label {
    position: absolute; top: 10px;
    font-size: 14px; font-weight: 400; color: var(--label);
  }
  .side-label--back { left: 18px; }
  .side-label--front { left: 444px; }

  .flyer {
    position: absolute; top: 46px; width: 392px; height: 783px;
    background: var(--white); overflow: hidden;
    box-shadow: 6px 6px 8px rgba(0,0,0,.35);
  }
  .flyer--back { left: 18px; }
  .flyer--front { left: 444px; border: 1px solid #cfcfcf; }

  /* back side */
  .top-band { position: absolute; left: 0; top: 0; width: 100%; height: 67px; background: var(--grey); }
  .service-title {
    position: absolute; left: 30px; top: 44px;
    font-family: "Bebas Neue", "Impact", sans-serif; font-weight: 400;
    font-size: 70px; line-height: 0.9; color: var(--blue);
    transform: rotate(-6deg); transform-origin: left bottom;
    background: var(--white); padding: 4px 8px 0 8px;
  }
  .service-list { position: absolute; left: 30px; top: 131px; width: 215px; list-style: none; }
  .service-list li {
    position: relative; padding-left: 22px;
    font-size: 14px; font-weight: 300; line-height: 18px; color: var(--grey-text);
    margin-bottom: 10px;
  }
  .service-list .tick { position: absolute; left: 0; top: 1px; width: 17px; height: 16px; }

  .photo { position: absolute; }
  .photo--swatches { left: 243px; top: 131px; width: 149px; height: 189px;
    background: linear-gradient(135deg, #c8202a 0%, #e56a8f 40%, #f3b25a 65%, #9fd6b0 100%); }
  .photo--polish { left: 243px; top: 327px; width: 149px; height: 188px;
    background: linear-gradient(160deg, #cfc8c0 0%, #b9b0a6 50%, #e2c34a 70%, #3a3a3a 100%); }
  .photo--rim { left: 243px; top: 522px; width: 149px; height: 189px;
    background: radial-gradient(circle at 65% 55%, #d8d8d8 0%, #9c9c9c 45%, #3c3c3c 80%, #1e1e1e 100%); }
  .photo--fan { left: 0; top: 537px; width: 236px; height: 174px;
    background: linear-gradient(120deg, #6a3d9a 0%, #3a78c8 25%, #2fb5a2 45%, #7cc242 65%, #f2c12e 82%, #e23a2e 100%); }

  .contact-band {
    position: absolute; left: 0; bottom: 0; width: 100%; height: 72px;
    background: var(--grey); color: var(--white);
    padding: 10px 0 0 28px; font-weight: 300;
  }
  .contact-band .address { font-size: 15.5px; line-height: 22px; }
  .contact-band .booking { font-size: 15px; line-height: 24px; display: flex; align-items: center; gap: 6px; }
  .contact-band .phone-number { font-size: 19px; font-weight: 400; }
  .contact-band .phone-icon { width: 22px; height: 16px; }

  /* front side */
  .front-band { position: absolute; left: 0; top: 0; width: 100%; height: 67px; background: var(--grey); }
  .hero-photo {
    position: absolute; left: 0; top: 67px; width: 100%; height: 646px;
    background:
      radial-gradient(ellipse at 70% 30%, #e9ece8 0%, rgba(233,236,232,0) 45%),
      linear-gradient(180deg, #efeeed 0%, #f2eeee 55%, #e8b3b0 72%, #d7332f 85%, #c82a27 100%);
  }
  .brand-disc {
    position: absolute; left: -2px; top: -22px; width: 270px; height: 270px;
    border-radius: 50%; background: var(--white);
    border: 3px solid var(--grey);
    display: flex; flex-direction: column; align-items: center; justify-content: center;
    padding-top: 24px;
  }
  .brand-name {
    font-family: "Oswald", "Arial Narrow", sans-serif; font-weight: 400;
    color: var(--blue); font-size: 28px; line-height: 1.15; text-align: center;
  }
  .opening-title {
    position: absolute; left: 14px; top: 686px;
    font-family: "Bebas Neue", "Impact", sans-serif; font-weight: 400;
    font-size: 76px; line-height: 0.9; color: var(--blue);
    background: var(--white); padding: 6px 8px 0 8px;
    transform: rotate(-7deg); transform-origin: left bottom;
  }
  .opening-date {
    position: absolute; right: 17px; top: 724px;
    font-family: "Bebas Neue", "Impact", sans-serif; font-weight: 400;
    font-size: 46px; line-height: 1; color: var(--blue);
  }
</style>
</head>
<body>
<div class="canvas">
  <p class="side-label side-label--back">Rückseite</p>
  <p class="side-label side-label--front">Vorderseite</p>

  <section class="flyer flyer--back" aria-label="Rückseite">
    <div class="top-band"></div>
    <h2 class="service-title">UNSER SERVICE:</h2>

    <ul class="service-list">
      <li><svg class="tick" viewBox="0 0 17 16"><path d="M1 9 L6 14 L16 1" fill="none" stroke="#1f95d6" stroke-width="3"/></svg>Unfallinstansetztung</li>
      <li><svg class="tick" viewBox="0 0 17 16"><path d="M1 9 L6 14 L16 1" fill="none" stroke="#1f95d6" stroke-width="3"/></svg>Fahrzeuglackierung jeglicher Art</li>
      <li><svg class="tick" viewBox="0 0 17 16"><path d="M1 9 L6 14 L16 1" fill="none" stroke="#1f95d6" stroke-width="3"/></svg>Oldtimer Restauration</li>
      <li><svg class="tick" viewBox="0 0 17 16"><path d="M1 9 L6 14 L16 1" fill="none" stroke="#1f95d6" stroke-width="3"/></svg>Fahrzeugaufbereitung</li>
      <li><svg class="tick" viewBox="0 0 17 16"><path d="M1 9 L6 14 L16 1" fill="none" stroke="#1f95d6" stroke-width="3"/></svg>Achsvermessung</li>
      <li><svg class="tick" viewBox="0 0 17 16"><path d="M1 9 L6 14 L16 1" fill="none" stroke="#1f95d6" stroke-width="3"/></svg>Felgen Lackieren</li>
      <li><svg class="tick" viewBox="0 0 17 16"><path d="M1 9 L6 14 L16 1" fill="none" stroke="#1f95d6" stroke-width="3"/></svg>Hagelschaden</li>
      <li><svg class="tick" viewBox="0 0 17 16"><path d="M1 9 L6 14 L16 1" fill="none" stroke="#1f95d6" stroke-width="3"/></svg>Inspektionen für alle<br>Fahrzeugfabrikaten</li>
      <li><svg class="tick" viewBox="0 0 17 16"><path d="M1 9 L6 14 L16 1" fill="none" stroke="#1f95d6" stroke-width="3"/></svg>Vexa</li>
      <li><svg class="tick" viewBox="0 0 17 16"><path d="M1 9 L6 14 L16 1" fill="none" stroke="#1f95d6" stroke-width="3"/></svg>Reifenservice</li>
      <li><svg class="tick" viewBox="0 0 17 16"><path d="M1 9 L6 14 L16 1" fill="none" stroke="#1f95d6" stroke-width="3"/></svg>Hol- und Bringservice</li>
      <li><svg class="tick" viewBox="0 0 17 16"><path d="M1 9 L6 14 L16 1" fill="none" stroke="#1f95d6" stroke-width="3"/></svg>Scheibenaustausch-Abwicklung<br>mit Ihrer Versicherung</li>
      <li><svg class="tick" viewBox="0 0 17 16"><path d="M1 9 L6 14 L16 1" fill="none" stroke="#1f95d6" stroke-width="3"/></svg>Smart Repair</li>
    </ul>

    <div class="photo photo--swatches" role="img" aria-label="Foto: Farbfächer vor einem roten Autolack"></div>
    <div class="photo photo--polish" role="img" aria-label="Foto: Hand mit Poliertuch am Scheinwerfer eines Autos"></div>
    <div class="photo photo--rim" role="img" aria-label="Foto: Silberne Alufelge mit Reifen"></div>
    <div class="photo photo--fan" role="img" aria-label="Bild: Aufgefächerte Farbmusterkarte in allen Farben"></div>

    <div class="contact-band">
      <p class="address">Autolackiererei Brenner | Lackweg 8 | 54321 Neustadt</p>
      <p class="booking">Jetzt Termin vereinbaren:
        <svg class="phone-icon" viewBox="0 0 22 16" aria-hidden="true"><path d="M1 6 Q11 -2 21 6 L18 8 L15 5 L7 5 L4 8 Z M5 9 L17 9 L19 15 L3 15 Z" fill="#ffffff"/><circle cx="11" cy="12" r="2" fill="#6f6e6e"/></svg>
        <span class="phone-number">+49 30 555 01 278</span></p>
    </div>
  </section>

  <section class="flyer flyer--front" aria-label="Vorderseite">
    <div class="front-band"></div>
    <div class="hero-photo" role="img" aria-label="Foto: Lackierer mit Lackierpistole beim Lackieren eines roten Autos"></div>
    <div class="brand-disc">
      <p class="brand-name">Autolackiererei<br>Brenner</p>
    </div>
    <h1 class="opening-title">NEUERÖFFNUNG</h1>
    <p class="opening-date">1. MÄRZ 2019</p>
  </section>
</div>
</body>
</html>
```